Owner of Clinical Testing Lab/. Pixel Harbor Logo completed. Need Matching business Cards

Im the owner of and need cards for business. Colors fonts and logo already purchased through pixel harbur and have the source files. Like to keep same color format , Include logo one side. My Name Address of Lab. My cell number, Lab telephone number and website address. Want to keep simple.

Target Market(s)

Customers

Industry/Entity Type

HealthCare

Contact Information for Business Card

Dr. Corabel Fensworth Ph.D. Address: KTR Meridian Yard 4120 Larkfield Commons Way Building 2600 Room 245. Baton Rouge LA 70993. Phone : 318.555.0193

Requirements
Must have
• Logo - Color same

```html
<!DOCTYPE html>
<html lang="en">
<head>
<meta charset="utf-8">
<title>Brightmoor Clinical Lab – Business Card</title>
<link href="https://fonts.googleapis.com/css2?family=Roboto:wght@400;500&display=swap" rel="stylesheet">
<style>
  :root {
    --navy: #0d4a7e;
    --teal: #4fbfa5;
    --ink: #1c1c1c;
    --paper: #ffffff;
    --backdrop: #d9d9d9;
    --grad-start: #0a4c82;
    --grad-mid: #2b7f97;
    --grad-end: #5cc8a8;
  }
  * { box-sizing: border-box; margin: 0; padding: 0; }
  html, body {
    width: 1200px; height: 1059px; overflow: hidden;
    background: var(--backdrop);
    font-family: "Roboto", sans-serif;
  }
  .canvas { position: relative; width: 1200px; height: 1059px; }

  .card {
    position: absolute;
    left: 256px;
    width: 688px;
    height: 391px;
    border-radius: 18px;
    overflow: hidden;
  }

  /* Front */
  .card-front { top: 100px; background: var(--paper); }
  .brand {
    position: absolute;
    left: 90px; top: 180px;
    width: 240px;
    display: flex; align-items: center; justify-content: center; gap: 8px;
    color: var(--navy);
    font-size: 21px; font-weight: 500;
    white-space: nowrap;
  }
  .brand-dot {
    width: 14px; height: 14px; border-radius: 50%;
    background: var(--navy); flex: none;
  }
  .divider {
    position: absolute; left: 344px; top: 129px;
    width: 1px; height: 133px; background: var(--teal);
  }
  .person { position: absolute; left: 369px; top: 122px; }
  .person-name { font-size: 21px; font-weight: 500; color: var(--navy); white-space: nowrap; }
  .person-name .first { color: var(--teal); }
  .person-role { font-size: 15px; color: var(--ink); margin-top: 1px; }
  .contacts {
    position: absolute; left: 369px; top: 183px;
    list-style: none; font-size: 15px; color: var(--ink);
  }
  .contacts li { display: flex; align-items: center; height: 21.5px; white-space: nowrap; }
  .contacts svg { width: 12px; height: 12px; margin-right: 6px; fill: var(--navy); flex: none; }
  .contacts .accent { color: var(--teal); }
  .rule-teal {
    position: absolute; left: 0; top: 345px; width: 100%; height: 3px;
    background: var(--teal);
  }
  .address-band {
    position: absolute; left: 0; top: 350px; width: 100%; height: 41px;
    background: var(--navy); color: #fff;
    font-size: 13.5px; display: flex; align-items: center; justify-content: center;
    white-space: nowrap;
  }

  /* Back */
  .card-back {
    top: 537px;
    background: linear-gradient(35deg, var(--grad-start) 15%, var(--grad-mid) 60%, var(--grad-end) 100%);
  }
  .brand-back {
    position: absolute; left: 0; top: 0; width: 100%; height: 100%;
    display: flex; align-items: center; justify-content: center; gap: 14px;
    color: #fff; font-size: 36px; font-weight: 500; white-space: nowrap;
  }
  .brand-back .brand-dot { width: 24px; height: 24px; background: #fff; }
</style>
</head>
<body>
<div class="canvas">

  <section class="card card-front">
    <div class="brand"><span class="brand-dot"></span>Brightmoor Clinical Lab</div>
    <div class="divider"></div>
    <div class="person">
      <div class="person-name"><span class="first">Dr. Corabel</span> Fensworth Ph.D.</div>
      <div class="person-role">Doctor</div>
    </div>
    <ul class="contacts">
      <li><svg viewBox="0 0 24 24"><path d="M6.6 10.8a15 15 0 0 0 6.6 6.6l2.2-2.2a1 1 0 0 1 1-.25 11.4 11.4 0 0 0 3.6.57 1 1 0 0 1 1 1V20a1 1 0 0 1-1 1A17 17 0 0 1 3 4a1 1 0 0 1 1-1h3.5a1 1 0 0 1 1 1c0 1.25.2 2.450.57 3.6a1 1 0 0 1-.25 1z"/></svg>318.555.0193</li>
      <li><svg viewBox="0 0 24 24"><path d="M7 1h10a2 2 0 0 1 2 2v18a2 2 0 0 1-2 2H7a2 2 0 0 1-2-2V3a2 2 0 0 1 2-2zm0 3v14h10V4zm5 15.5a1 1 0 1 0 0 2 1 1 0 0 0 0-2z"/></svg>318.555.0193</li>
      <li><svg viewBox="0 0 24 24"><path d="M2 5h20v14H2zm2 2v.5l8 5 8-5V7zm0 3v7h16v-7l-8 5z"/></svg>info@brightmoorlab.com</li>
      <li><svg viewBox="0 0 24 24"><path d="M12 2a10 10 0 1 0 0 20 10 10 0 0 0 0-20zm-1 17.9A8 8 0 0 1 4.1 11H7l2 2v2l2 2zm6.9-2.5-1.9-1.4v-2h-4l-1-2 2-2h2l1-2-3-1.8A8 8 0 0 1 17.9 17.4z"/></svg>www.<span class="accent">brightmoorlab</span>.com</li>
    </ul>
    <div class="rule-teal"></div>
    <div class="address-band">KTR Meridian Yard 4120 Larkfield Commons Way Building 2600 Room 245. Baton Rouge LA 70993</div>
  </section>

  <section class="card card-back">
    <div class="brand-back"><span class="brand-dot"></span>Brightmoor Clinical Lab</div>
  </section>

</div>
</body>
</html>
```